Postcard Design

the main information for my text is:
Harriet Lindqvist, MD
Board Certified Adult Psychiatrist
New patient appointments within 1-2 weeks
For new appointments, have patients go to:
www. brambleoakpsychiatry.example

(my address for the back) Harriet Lindqvist, MD
2718 West Halloway, Suite 405
Little Rock, AR 72207

```html
<!DOCTYPE html>
<html lang="en">
<head>
<meta charset="utf-8">
<title>Bramble Oak Psychiatry Postcard</title>
<link href="https://fonts.googleapis.com/css2?family=Oswald:wght@400;500;600;700&family=Open+Sans:ital,wght@0,400;0,600;0,700;1,400&display=swap" rel="stylesheet">
<style>
  :root {
    --page: #5f5a55;
    --red: #c8102e;
    --red-dark: #9e0c24;
    --charcoal: #2b2b2d;
    --charcoal-soft: #3a3a3d;
    --sand: #e8dfcf;
    --paper: #ffffff;
    --card-grey: #ecebe8;
    --ink: #333333;
    --muted: #666666;
    --stamp: #d9d9d9;
  }
  * { box-sizing: border-box; margin: 0; padding: 0; }
  html, body { width: 900px; height: 1200px; overflow: hidden; }
  body {
    background: var(--page);
    font-family: "Open Sans", Arial, sans-serif;
    position: relative;
  }
  .postcard {
    position: absolute;
    left: 45px;
    width: 810px;
    overflow: hidden;
    box-shadow: 0 4px 14px rgba(0,0,0,.35);
  }
  .postcard--front { top: 20px; height: 580px; background: var(--card-grey); }
  .postcard--back { top: 625px; height: 555px; background: var(--paper); }

  /* front top */
  .front-header {
    position: absolute; left: 0; top: 0; width: 810px; height: 285px;
    background: var(--charcoal);
  }
  .hero-photo {
    position: absolute; right: 0; top: 0; width: 380px; height: 285px;
    background: linear-gradient(120deg, #1e1e20 0%, #55575a 55%, #8a8c8f 100%);
  }
  .brand-banner {
    position: absolute; left: 0; top: 16px; width: 330px; height: 46px;
    background: var(--red);
    clip-path: polygon(0 0, 100% 0, 94% 100%, 0 100%);
    display: flex; align-items: center; padding-left: 24px;
  }
  .brand-name {
    font-family: "Oswald", sans-serif; font-weight: 500;
    color: var(--paper); font-size: 26px; letter-spacing: .5px;
  }
  .service-list {
    position: absolute; left: 26px; top: 78px;
    display: grid; grid-template-columns: 205px 170px; column-gap: 8px; row-gap: 2px;
    list-style: none; color: var(--paper); font-size: 11px; line-height: 1.45;
  }
  .service-list li { white-space: nowrap; }
  .service-list li::before {
    content: ""; display: inline-block; width: 5px; height: 5px;
    background: var(--red); margin-right: 7px; vertical-align: middle;
  }
  .headline {
    position: absolute; left: 26px; top: 186px; font-family: "Oswald", sans-serif;
    text-transform: uppercase; line-height: 1;
  }
  .headline__lead { color: var(--paper); font-size: 30px; font-weight: 500; display: block; }
  .headline__accent { color: var(--red); font-size: 52px; font-weight: 700; display: block; margin-top: 4px; }

  /* front body */
  .intro-panel {
    position: absolute; left: 0; top: 298px; width: 410px; height: 218px;
    background: var(--sand); padding: 22px 24px 0 26px;
  }
  .intro-panel p { font-size: 15.5px; line-height: 1.4; color: var(--ink); }
  .hours {
    position: absolute; left: 0; bottom: 18px; padding-left: 26px;
    font-family: "Oswald", sans-serif; font-weight: 500; color: var(--red);
    font-size: 17px; text-transform: uppercase;
  }
  .doctor-card {
    position: absolute; left: 424px; top: 298px; width: 370px; height: 218px;
    background: var(--paper); padding: 16px;
  }
  .doctor-photo {
    position: absolute; left: 16px; top: 16px; width: 92px; height: 96px;
    background: linear-gradient(160deg, #b9a08c, #6e4a3a);
  }
  .doctor-name {
    position: absolute; left: 120px; top: 22px;
    font-family: "Oswald", sans-serif; font-size: 25px; font-weight: 500; color: var(--ink);
  }
  .doctor-title {
    position: absolute; left: 120px; top: 60px; font-size: 12px; color: var(--red); font-weight: 600;
  }
  .doctor-note {
    position: absolute; left: 120px; top: 84px; width: 235px;
    font-size: 10px; font-style: italic; line-height: 1.35; color: var(--muted);
  }
  .doctor-exclusion {
    position: absolute; left: 120px; top: 150px; font-size: 14px; color: var(--red);
  }

  .web-bar {
    position: absolute; left: 0; bottom: 0; width: 100%; height: 50px;
    background: var(--red); color: var(--paper);
    display: flex; align-items: center; justify-content: center;
    font-size: 16px; font-weight: 600;
  }

  /* back */
  .stamp-box {
    position: absolute; right: 30px; top: 22px; width: 80px; height: 80px; background: var(--stamp);
  }
  .welcome {
    position: absolute; left: 30px; top: 28px; font-family: "Oswald", sans-serif;
    text-transform: uppercase; line-height: 1;
  }
  .welcome__lead { display: block; font-size: 76px; font-weight: 600; color: var(--charcoal); }
  .welcome__name { display: block; font-size: 40px; font-weight: 600; color: var(--red); margin-top: 6px; }
  .back-shapes { position: absolute; left: 0; top: 0; }
  .back-brand {
    position: absolute; left: 30px; top: 206px;
    font-family: "Oswald", sans-serif; font-weight: 500; font-size: 30px; color: var(--paper);
  }
  .appointment-info {
    position: absolute; left: 30px; top: 290px; color: var(--paper);
  }
  .appointment-info p { font-size: 20px; line-height: 1.3; }
  .appointment-info .url { margin-top: 8px; font-size: 21px; font-weight: 600; }
  .appointment-info address { font-style: normal; margin-top: 24px; font-size: 20px; line-height: 1.35; }
</style>
</head>
<body>

<section class="postcard postcard--front" aria-label="Postcard front">
  <div class="front-header">
    <div class="hero-photo" role="img" aria-label="Photo of a man in a dark shirt sketching a brain outline on a glass board"></div>
    <div class="brand-banner"><span class="brand-name">Bramble Oak Psychiatry</span></div>
    <ul class="service-list">
      <li>Major Depressive Disorders</li>
      <li>Self Esteem Issues</li>
      <li>Grief and Loss Issues</li>
      <li>Women's Mood Disorders</li>
      <li>Bipolar Disorders</li>
      <li>Stress Management</li>
      <li>Divorce / Relationship Problems</li>
      <li>Substance Problems</li>
      <li>Anxiety Disorders</li>
    </ul>
    <h1 class="headline">
      <span class="headline__lead">New Patient Appointments</span>
      <span class="headline__accent">Within 1-2 Weeks</span>
    </h1>
  </div>

  <div class="intro-panel">
    <p>Seeking care from a psychiatrist can be a difficult decision, as mental health issues can be associated with negative feelings. Due to the sensitive nature of the problems being addressed, confidentiality is the highest priority in my practice.</p>
    <div class="hours">Hours by appointment - (501) 555-0147</div>
  </div>

  <div class="doctor-card">
    <div class="doctor-photo" role="img" aria-label="Portrait photo of the psychiatrist"></div>
    <div class="doctor-name">Harriet Lindqvist M.D.</div>
    <div class="doctor-title">Board Certified Adult Psychiatrist</div>
    <p class="doctor-note">"Treatment with me would never be shared with any entities, including your insurance company, unless you request it."</p>
    <div class="doctor-exclusion">I do not treat ADHD or ADD</div>
  </div>

  <div class="web-bar">Visit our website to know more informations at - www.brambleoakpsychiatry.example</div>
</section>

<section class="postcard postcard--back" aria-label="Postcard back">
  <svg class="back-shapes" width="810" height="555" viewBox="0 0 810 555" aria-hidden="true">
    <polygon points="0,250 560,250 640,505 0,505" fill="var(--charcoal)"/>
    <polygon points="548,250 572,250 652,505 628,505" fill="var(--red)"/>
    <polygon points="590,150 614,150 732,505 708,505" fill="var(--red)"/>
    <polygon points="0,198 585,198 565,250 0,250" fill="var(--red)"/>
  </svg>
  <div class="stamp-box"></div>
  <h2 class="welcome">
    <span class="welcome__lead">Welcome to</span>
    <span class="welcome__name">Bramble Oak Psychiatry</span>
  </h2>
  <div class="back-brand">Bramble Oak Psychiatry</div>
  <div class="appointment-info">
    <p>For new appointments,<br>have patients go to:</p>
    <p class="url">www. brambleoakpsychiatry.example</p>
    <address>2718 West Halloway, Suite 405<br>Little Rock, AR 72207</address>
  </div>
  <div class="web-bar">Visit our website to know more informations at - www.brambleoakpsychiatry.example</div>
</section>

</body>
</html>
```